LOLU Baby Massage Classes - flyer to make a difference

I need a single page flyer, preferably single page, to hand out to doctors, medical centres and parents. To also leave on counters of establishments.
It is to promote my baby massage classes. Mums can get together with other mums and book a 5 week course to learn and discover the many benefits of baby massage.
Benefits include: enhances bonding and attachment, understand non-verbal cues from your baby, helps with sleep patterns, help with immune system, increases vagal activity,relief from wind, colic or constipation to name some.

Baby age from birth to 12 months. Group classes or private sessions

I am a Professional Member and Certified by the Global Society of Newborn Touch (GSNT) GSNT Australia is Nationally Accredited and is endorsed by Crown Academy of Carers, the Southern Guild of Birth Attendants, The Southern Union of Daily Living Therapy Australia, The Southern Union of Bodywork Practitioner and is a full member of Wellmind Network Australia.

Class detail and availability contact is Petra Holm 0487 315 208 petra.joanne.holm@quillmail.example www.lolunewborntouch com.au facebook/comLOLUnewborntouch

My colour scheme is green and purple as you will see from my logo and website. I would like my flyer to be softer tones of either both colours or just one.

I will include some images you can choose from or show me any you think will fit in with baby massage. THANK YOU
Updates

Hi The size of my flyer is A6. Approx 150mms x 210mms and single sided. Thank you

Target Market(s)

mums and dads, groups, doctors, midwives

Industry/Entity Type

Medical

Font styles to use
Sans Serif

Colors
87d0c7
b09cc8

Requirements
Must have
• baby photo or photos, both my logo and the GSNT logo. The GSNT logo is to be small
• Baby Massage Classes (wording) is very important to catch the eye.
• Invitation to book a class or gather friends to book is next in importance
• Benefits is next
• The admin information ie.,membership, certification and endorsements are lesser and can be small.
• Contact information to be noticeable.
Nice to have
• If you have an idea, drawing or photo that would look better, please feel free to try it
Should not have
• should not be crowded with information all the same size

```html
<!DOCTYPE html>
<html lang="en">
<head>
<meta charset="utf-8">
<title>LOLU Baby Massage Classes</title>
<link rel="stylesheet" href="https://fonts.googleapis.com/css2?family=Arimo:wght@400;700&display=swap">
<style>
  :root {
    --teal: #1fa596;
    --teal-soft: #87d0c7;
    --purple: #7d2b8f;
    --purple-soft: #b09cc8;
    --grey: #8b8584;
    --grey-dark: #6f6968;
    --white: #ffffff;
  }
  * { box-sizing: border-box; margin: 0; padding: 0; }
  html, body { width: 925px; height: 1200px; overflow: hidden; background: var(--white); }
  body { font-family: "Arimo", Arial, sans-serif; position: relative; }
  .flyer { position: relative; width: 925px; height: 1200px; overflow: hidden; background: var(--white); }

  .brand { position: absolute; left: 45px; top: 50px; display: flex; align-items: center; gap: 22px; }
  .brand-dot { width: 120px; height: 120px; border-radius: 50%; background: var(--teal-soft); }
  .brand-name { font-size: 72px; font-weight: 700; color: var(--purple); letter-spacing: 1px; }

  .header-rule { position: absolute; left: 470px; top: 50px; width: 2px; height: 160px; background: var(--purple-soft); }

  .age-swoosh { position: absolute; left: 520px; top: 30px; width: 360px; height: 170px; }
  .age-label { position: absolute; left: 555px; top: 80px; font-size: 27px; font-weight: 700; color: var(--teal); transform: rotate(-14deg); transform-origin: left center; }
  .website { position: absolute; left: 500px; top: 198px; font-size: 25px; font-weight: 700; color: var(--grey); }

  .headline { position: absolute; left: 0; width: 925px; top: 240px; text-align: center; font-size: 68px; font-weight: 700; color: var(--teal); }
  .subhead { position: absolute; left: 0; width: 925px; top: 322px; text-align: center; font-size: 29px; font-weight: 700; color: var(--purple); }

  .photo { position: absolute; left: 0; top: 370px; width: 925px; height: 380px;
    background: radial-gradient(ellipse at 55% 45%, #f3d9c8 0%, #f6e6dc 40%, #fbf5f1 70%, var(--white) 100%); }

  .benefits { position: absolute; left: 40px; top: 720px; list-style: none; }
  .benefits li { display: flex; align-items: center; gap: 8px; font-size: 24px; font-weight: 700; color: var(--grey-dark); line-height: 30px; }
  .tick { width: 20px; height: 20px; flex: none; }
  .more { position: absolute; left: 490px; top: 895px; font-size: 22px; font-weight: 700; color: var(--teal); }

  .course { position: absolute; left: 650px; top: 690px; width: 260px; height: 200px; }
  .course-num { position: absolute; left: 20px; top: 0; font-size: 170px; font-weight: 700; color: var(--purple); line-height: 1; }
  .course-swoosh { position: absolute; left: 0; top: 60px; width: 260px; height: 150px; }
  .course-label { position: absolute; left: 28px; top: 150px; font-size: 24px; font-weight: 700; color: var(--teal); transform: rotate(-48deg); transform-origin: left center; }
  .benefits-title { position: absolute; left: 660px; top: 880px; font-size: 50px; font-weight: 700; color: var(--purple); }

  .contact-band { position: absolute; left: 0; top: 945px; width: 925px; height: 90px; background: var(--teal); }
  .portrait { position: absolute; left: 40px; top: 895px; width: 135px; height: 150px; background: linear-gradient(160deg, #9bb48a 0%, #c9d6b8 50%, #8e5aa5 100%); border: 3px solid var(--white); }
  .book-tag { position: absolute; left: 182px; top: 900px; height: 42px; display: flex; align-items: center; gap: 12px; padding: 0 16px; background: var(--purple); color: var(--white); font-size: 26px; font-weight: 700; }
  .book-tag svg { width: 22px; height: 16px; }
  .book-tag .split { width: 2px; height: 26px; background: var(--purple-soft); }
  .contact-name { position: absolute; left: 195px; top: 968px; font-size: 42px; font-weight: 700; color: var(--white); }
  .contact-rule { position: absolute; left: 478px; top: 955px; width: 2px; height: 70px; background: var(--white); opacity: .7; }
  .contact-line { position: absolute; left: 495px; display: flex; align-items: center; gap: 12px; color: var(--white); font-weight: 700; }
  .contact-line svg { width: 26px; height: 26px; flex: none; }
  .phone { top: 952px; font-size: 34px; }
  .email { top: 998px; font-size: 20px; }

  .badge { position: absolute; left: 55px; top: 1070px; width: 70px; height: 70px; border-radius: 50%; background: var(--purple-soft); }
  .certified { position: absolute; left: 195px; top: 1050px; font-size: 20px; font-weight: 700; color: var(--purple); }
  .endorsements { position: absolute; left: 195px; top: 1080px; width: 690px; font-size: 15px; line-height: 19px; color: var(--grey); }
</style>
</head>
<body>
<main class="flyer">
  <header>
    <div class="brand">
      <span class="brand-dot"></span>
      <span class="brand-name">lolu</span>
    </div>
    <div class="header-rule"></div>
    <svg class="age-swoosh" viewBox="0 0 360 170" aria-hidden="true">
      <path d="M10 40 Q 170 220 350 10 Q 200 150 10 40 Z" fill="var(--grey)"/>
    </svg>
    <div class="age-label">Birth to 12 Months</div>
    <div class="website">lolunewborntouch com.au</div>
  </header>

  <h1 class="headline">Baby Massage Classes</h1>
  <p class="subhead">Group Classes / Private Sessions</p>

  <div class="photo" role="img" aria-label="Photo of a smiling baby lying on a white sheet while an adult's hands massage its legs"></div>

  <ul class="benefits">
    <li><svg class="tick" viewBox="0 0 20 20"><path d="M3 11 L8 16 L17 4" fill="none" stroke="var(--purple)" stroke-width="3" stroke-linecap="round"/></svg>Enhances bonding and attachment</li>
    <li><svg class="tick" viewBox="0 0 20 20"><path d="M3 11 L8 16 L17 4" fill="none" stroke="var(--purple)" stroke-width="3" stroke-linecap="round"/></svg>Understand non-verbal cues from your baby</li>
    <li><svg class="tick" viewBox="0 0 20 20"><path d="M3 11 L8 16 L17 4" fill="none" stroke="var(--purple)" stroke-width="3" stroke-linecap="round"/></svg>Helps with sleep patterns</li>
    <li><svg class="tick" viewBox="0 0 20 20"><path d="M3 11 L8 16 L17 4" fill="none" stroke="var(--purple)" stroke-width="3" stroke-linecap="round"/></svg>Help with immune system</li>
    <li><svg class="tick" viewBox="0 0 20 20"><path d="M3 11 L8 16 L17 4" fill="none" stroke="var(--purple)" stroke-width="3" stroke-linecap="round"/></svg>Increases vagal activity</li>
    <li><svg class="tick" viewBox="0 0 20 20"><path d="M3 11 L8 16 L17 4" fill="none" stroke="var(--purple)" stroke-width="3" stroke-linecap="round"/></svg>Relief from wind, colic or constipation</li>
  </ul>
  <div class="more">and more....</div>

  <div class="course">
    <svg class="course-swoosh" viewBox="0 0 260 150" aria-hidden="true">
      <path d="M20 130 Q 200 150 240 10 Q 220 160 20 130 Z" fill="var(--grey)"/>
    </svg>
    <div class="course-num">5</div>
    <div class="course-label">week course</div>
  </div>
  <div class="benefits-title">Benefits</div>

  <section class="contact">
    <div class="contact-band"></div>
    <div class="portrait" role="img" aria-label="Portrait photo of the instructor in a purple top in a garden"></div>
    <div class="book-tag">BOOK NOW <span class="split"></span>
      <svg viewBox="0 0 22 16"><path d="M2 3 H20 L11 14 Z" fill="var(--white)"/></svg>
    </div>
    <div class="contact-name">Petra Holm</div>
    <div class="contact-rule"></div>
    <div class="contact-line phone">
      <svg viewBox="0 0 24 24"><path d="M6.6 10.8a15 15 0 0 0 6.6 6.6l2.2-2.2a1 1 0 0 1 1-.25 11.4 11.4 0 0 0 3.6.57 1 1 0 0 1 1 1V20a1 1 0 0 1-1 1A17 17 0 0 1 3 4a1 1 0 0 1 1-1h3.5a1 1 0 0 1 1 1c0 1.25.2 2.45.57 3.6a1 1 0 0 1-.25 1z" fill="var(--white)"/></svg>
      0487 315 208
    </div>
    <div class="contact-line email">
      <svg viewBox="0 0 24 24"><rect x="2" y="5" width="20" height="14" rx="1" fill="none" stroke="var(--white)" stroke-width="2"/><path d="M2 6 L12 13 L22 6" fill="none" stroke="var(--white)" stroke-width="2"/></svg>
      petra.joanne.holm@quillmail.example
    </div>
  </section>

  <footer>
    <div class="badge"></div>
    <p class="certified">Certified by the Global Society of Newborn Touch (GSNT)</p>
    <p class="endorsements">GSNT Australia is Nationally Accredited and is endorsed by Crown Academy of Carers, the Southern Guild of Birth Attendants, The Southern Union of Daily Living Therapy Australia, The Southern Union of Bodywork Practitioner and is a full member of Wellmind Network Australia.</p>
  </footer>
</main>
</body>
</html>
```